Harborline Hire Business Card Design

Need business cards designed for our new equipment rental. We specialize in renting to landscape / tree professionals, contractors, Do-It-Yourself'ers and Around the home or office. Looking for a eye catching card. Landscape and construction should be the theme. The logo is attached, and you can see our colors from the logo. You can use whatever color goes with it ok.

Target Market(s)

First off Landscape and Tree Professional. Then contractors, Do-It-Yourself'ers and rentals for Around the home or office.

Industry/Entity Type

Business

Contact Information for Business Card

Eye catching background that blends landscaping with construction equipment

Requirements
Must have
• Name on Card will Be: Martin Kolbeck (Manager)
• My Direct Phone Number is: 352-817-3062
• martin@harborlinehire.com
• www.harborlinehire.com
• 4712 Willow Brook Lane,
• Dade City FL 33590
Nice to have
• Would be Nice to have these bullets on the Face of the card that does not have all my information.
• Serving:
• Landscape / Tree Professionals
• Contractors
• DYI'ers or say Do-It-Yourself'ers
• Maybe have serving small and centered above these bullets, and these 3 bullets along the bottom of the card. Ideas?

```html
<!DOCTYPE html>
<html lang="en">
<head>
<meta charset="utf-8">
<title>Harborline Hire Business Card</title>
<link rel="stylesheet" href="https://fonts.googleapis.com/css2?family=Open+Sans:wght@400;600;700&display=swap">
<style>
  :root {
    --navy: #033a5e;
    --orange: #e9a650;
    --paper: #f2f2f2;
    --backdrop: #c4c4c4;
    --white: #ffffff;
  }
  * { margin: 0; padding: 0; box-sizing: border-box; }
  html, body { width: 1200px; height: 576px; overflow: hidden; }
  body {
    background: var(--backdrop);
    font-family: "Open Sans", Arial, sans-serif;
    position: relative;
  }
  .card {
    position: absolute;
    border-radius: 14px;
    overflow: hidden;
    box-shadow: 0 3px 8px rgba(0,0,0,0.25);
  }
  .card-front {
    left: 82px; top: 139px; width: 484px; height: 291px;
    background: var(--navy);
  }
  .card-back {
    left: 602px; top: 138px; width: 481px; height: 291px;
    background: var(--paper);
  }
  .brand-name {
    position: absolute;
    font-weight: 700;
    white-space: nowrap;
    transform: translate(-50%, -50%);
    letter-spacing: 0.5px;
  }
  .card-front .brand-name {
    left: 242px; top: 133px;
    font-size: 38px;
    color: var(--orange);
  }
  .front-web {
    position: absolute;
    left: 0; right: 0; top: 262px;
    display: flex; justify-content: center; align-items: center; gap: 14px;
    font-size: 12.5px; color: var(--white);
  }
  .front-web .rule { width: 62px; height: 1px; background: var(--orange); }
  .front-web .accent { color: var(--orange); }
  .back-shape { position: absolute; inset: 0; }
  .card-back .brand-name {
    left: 363px; top: 146px;
    font-size: 22px;
    color: var(--navy);
  }
  .person { position: absolute; left: 24px; top: 42px; color: var(--white); }
  .person-name { font-size: 18px; font-weight: 600; line-height: 24px; }
  .person-role { font-size: 12.5px; margin-top: 2px; }
  .address {
    position: absolute; left: 24px; top: 178px;
    color: var(--white); font-size: 12.5px; line-height: 16px;
  }
  .contacts {
    position: absolute; left: 24px; top: 220px;
    list-style: none; color: var(--white); font-size: 12.5px;
  }
  .contacts li { display: flex; align-items: center; height: 17px; }
  .contacts svg { width: 10px; height: 10px; margin-right: 12px; fill: var(--orange); flex: none; }
</style>
</head>
<body>

<section class="card card-front">
  <div class="brand-name">Harborline Hire</div>
  <div class="front-web">
    <span class="rule"></span>
    <span>www.<span class="accent">harborlinehire</span>.com</span>
    <span class="rule"></span>
  </div>
</section>

<section class="card card-back">
  <svg class="back-shape" viewBox="0 0 481 291" preserveAspectRatio="none" aria-hidden="true">
    <path d="M0 0 H294 Q236 146 292 291 H0 Z" fill="var(--orange)"/>
    <path d="M0 0 H284 Q226 146 282 291 H0 Z" fill="var(--navy)"/>
    <path d="M0 41 A16 16 0 0 1 0 73 Z" fill="var(--orange)"/>
  </svg>

  <div class="person">
    <div class="person-name">Martin Kolbeck</div>
    <div class="person-role">Manager</div>
  </div>

  <div class="address">
    4712 Willow Brook Lane,<br>
    Dade City FL 33590
  </div>

  <ul class="contacts">
    <li>
      <svg viewBox="0 0 10 10"><path d="M1 3 Q5 0 9 3 L8 4.5 L6.5 3.8 V3 H3.5 V3.8 L2 4.5 Z M2.5 5 H7.5 L8.5 9 H1.5 Z"/></svg>
      352-817-3062
    </li>
    <li>
      <svg viewBox="0 0 10 10"><circle cx="5" cy="5" r="4.5" fill="none" stroke="var(--orange)" stroke-width="1"/><path d="M0.5 5 H9.5 M5 0.5 V9.5" stroke="var(--orange)" stroke-width="0.8"/><ellipse cx="5" cy="5" rx="2" ry="4.5" fill="none" stroke="var(--orange)" stroke-width="0.8"/></svg>
      www.harborlinehire.com
    </li>
    <li>
      <svg viewBox="0 0 10 10"><rect x="0.5" y="2" width="9" height="6.5"/><path d="M0.5 2 L5 5.8 L9.5 2" fill="none" stroke="var(--navy)" stroke-width="0.8"/></svg>
      martin@harborlinehire.com
    </li>
  </ul>

  <div class="brand-name">Harborline Hire</div>
</section>

</body>
</html>
```